【 概要 】 ナイトワーク専門のスキマバイトアプリを運営しています。事業者への訴求に特化した広告バナーを制作いただきたく思います。 【 依頼内容 】 ・サイズ: 横1080px × 縦1080px ・作成数: 1種類 ・利用用途:SNS広告など 【 デザインイメージ 】 ・ホームページデザインに似たテイスト / https://about.velto-rinka.jp ・「ナイトワーク人材足りてますか?」というテキストを強調表示 【 契約金額(税抜) 】 10,000円 / 1枚 ※契約金額(税込)からシステム利用料を差し引いた金額が、ワーカーさまの受取金額となります その他ご質問等ありましたら、気軽にお問い合わせください。 ご応募をお待ちしております。 |
どの案も素敵でしたが、この作品が最もイメージに合っていました。
この度は沢山のご応募を誠にありがとうございました。
不採用の場合でもめぼしい作品は買い取らせていただければと考えていますので、対象者には追ってご連絡させていただきます。その他、実績として制作物の掲載をご希望の方がいらっしゃいましたら、承認制にはなりますがご連絡ください。
今後ともよろしくお願いいたします。

```html
<!DOCTYPE html>
<html lang="ja">
<head>
<meta charset="utf-8">
<title>ナイトワーク人材 足りてますか?</title>
<link rel="stylesheet" href="https://fonts.googleapis.com/css2?family=Noto+Sans+JP:wght@500;700;900&display=swap">
<style>
  :root {
    --navy: #1f2a6b;
    --navy-deep: #141c4d;
    --ink: #111318;
    --orange: #f39a1e;
    --white: #ffffff;
    --paper: #f6f7fa;
    --grey: #c9cdd8;
  }
  * { box-sizing: border-box; margin: 0; padding: 0; }
  html, body { width: 1200px; height: 1200px; overflow: hidden; }
  body {
    font-family: "Noto Sans JP", sans-serif;
    background: var(--white);
    color: var(--ink);
  }
  .banner {
    position: relative;
    width: 1200px;
    height: 1200px;
    overflow: hidden;
    background: linear-gradient(180deg, var(--paper) 0%, var(--white) 40%);
  }
  .megaphone {
    position: absolute;
    left: 52px;
    top: 140px;
    width: 120px;
    height: 100px;
  }
  .hashtag {
    position: absolute;
    left: 210px;
    top: 60px;
    transform: rotate(-7deg);
    transform-origin: left top;
  }
  .hashtag-line {
    display: inline-block;
    font-weight: 900;
    font-size: 44px;
    line-height: 1;
    padding: 10px 22px;
    background: var(--white);
    border: 3px solid var(--ink);
    color: var(--ink);
  }
  .hashtag-line.accent {
    display: block;
    margin: 6px 0 0 110px;
    width: max-content;
    color: var(--orange);
    border-color: var(--orange);
  }
  .brand {
    position: absolute;
    right: 36px;
    top: 18px;
    display: flex;
    align-items: center;
    gap: 14px;
    color: var(--navy);
    font-weight: 900;
    font-size: 34px;
    line-height: 1.05;
  }
  .brand-mark {
    width: 48px;
    height: 48px;
    background: var(--navy);
  }
  .headline {
    position: absolute;
    left: 62px;
    top: 240px;
    font-weight: 900;
    font-size: 128px;
    line-height: 1.18;
    letter-spacing: 2px;
    color: var(--ink);
    text-shadow: 0 6px 0 var(--grey);
  }
  .figure {
    position: absolute;
    left: 690px;
    top: 490px;
    width: 500px;
    height: 600px;
    border-radius: 220px 220px 0 0;
    background: linear-gradient(160deg, #e9ebf2 0%, #9aa2bd 45%, var(--navy-deep) 100%);
  }
  .benefits {
    position: absolute;
    left: 93px;
    top: 620px;
    list-style: none;
    display: flex;
    flex-direction: column;
    gap: 46px;
  }
  .benefit {
    position: relative;
    width: 574px;
    height: 88px;
    border-radius: 44px;
    background: var(--navy);
    color: var(--white);
    display: flex;
    flex-direction: column;
    align-items: center;
    justify-content: center;
    padding-left: 60px;
    box-shadow: 0 6px 0 var(--navy-deep);
  }
  .benefit-tick {
    position: absolute;
    left: 44px;
    top: 22px;
    width: 46px;
    height: 44px;
  }
  .benefit-note {
    font-weight: 700;
    font-size: 22px;
    line-height: 1;
    margin-bottom: 4px;
  }
  .benefit-main {
    font-weight: 700;
    font-size: 46px;
    line-height: 1;
  }
  .cta-band {
    position: absolute;
    left: 0;
    bottom: 0;
    width: 1200px;
    height: 152px;
    background: linear-gradient(90deg, var(--navy-deep) 0%, var(--navy) 100%);
    border-top: 6px solid var(--grey);
    color: var(--white);
    display: flex;
    flex-direction: column;
    justify-content: center;
    padding-left: 50px;
    width: 1200px;
  }
  .cta-text {
    width: 1080px;
    text-align: left;
    padding-left: 0;
  }
  .cta-line {
    display: block;
    font-weight: 700;
    font-size: 50px;
    line-height: 1.2;
    width: 1080px;
    text-align: left;
  }
  .cta-line.first { padding-left: 220px; }
</style>
</head>
<body>
<main class="banner">
  <svg class="megaphone" viewBox="0 0 120 100" aria-hidden="true">
    <g fill="none" stroke="#111318" stroke-width="5" stroke-linejoin="round" stroke-linecap="round">
      <path d="M20 40 L60 40 L95 18 L95 82 L60 60 L20 60 Z"/>
      <path d="M32 60 L40 88 L54 88 L48 60"/>
      <path d="M104 34 L116 28 M106 50 L118 50 M104 66 L116 72"/>
    </g>
  </svg>

  <div class="hashtag">
    <span class="hashtag-line">#闇バイトやめて</span>
    <span class="hashtag-line accent">ナイトワークやれ!!</span>
  </div>

  <div class="brand">
    <span class="brand-mark"></span>
    <span class="brand-name">Velto<br>Rinka</span>
  </div>

  <h1 class="headline">ナイトワーク人材<br>足りてますか?</h1>

  <div class="figure" role="img" aria-label="スーツ姿で手を差し出して案内する男性のイラスト"></div>

  <ul class="benefits">
    <li class="benefit">
      <svg class="benefit-tick" viewBox="0 0 46 44" aria-hidden="true"><path d="M4 24 L17 38 L42 6" fill="none" stroke="#fff" stroke-width="7" stroke-linecap="round" stroke-linejoin="round"/></svg>
      <span class="benefit-main">高時給</span>
    </li>
    <li class="benefit">
      <svg class="benefit-tick" viewBox="0 0 46 44" aria-hidden="true"><path d="M4 24 L17 38 L42 6" fill="none" stroke="#fff" stroke-width="7" stroke-linecap="round" stroke-linejoin="round"/></svg>
      <span class="benefit-note">お金は</span>
      <span class="benefit-main">即日入金</span>
    </li>
    <li class="benefit">
      <svg class="benefit-tick" viewBox="0 0 46 44" aria-hidden="true"><path d="M4 24 L17 38 L42 6" fill="none" stroke="#fff" stroke-width="7" stroke-linecap="round" stroke-linejoin="round"/></svg>
      <span class="benefit-note">面接・履歴書</span>
      <span class="benefit-main">不要</span>
    </li>
  </ul>

  <footer class="cta-band">
    <p class="cta-text">
      <span class="cta-line first">高時給!</span>
      <span class="cta-line">ナイトワークのスキマバイト!</span>
    </p>
  </footer>
</main>
</body>
</html>
```